Project Management - Web Design Project

Valtrix 4 Management Limited is a company which provides specialist Project Control and Contract Management expertise to the Engineering, Construction and Manufacturing industries. The emphasis is on advanced Project Management techniques in particular Planning & Scheduling, Cost Control, Change Control, Risk Management, Reporting and Contract Administration. We are a global company (albeit a small start-up at this time) and pride ourselves on our ability to support projects to help them achieve their goals and objectives. Our aim is to implement work class control tools in a simple and user friendly manner. We would like the website to appear professional but at the same time easy to navigate and a good balance between text and pictures. The final design should communicate our value added service to our customers, our willingness to support and our structured approach to our work.

Target Market(s)

Project Management professionals working for engineering, construction and manufacturing organisations involved with delivering projects.

Industry/Entity Type

Construction

Requirements
Must have
• The website must include all of the content from the attached Excel brief. The company logo (attached) must also be included in the design. The design must portray a professional look and feel. Please include pictures and photographs related to project management in the engineering, construction and manufacturing industries. We may supplement with pictures of our own during the next steps.
Nice to have
• Emphasis that Valtrix 4 is available to support, guide, direct to achieve positive outcomes for the projects. We work hard at developing our customer relationships. Our employees are experienced in advanced project management techniques.
Should not have
• The design should not use old style fonts. It should look modern and professional. Do not include cartoons or silly illustrations.

```html
<!DOCTYPE html>
<html lang="en">
<head>
<meta charset="utf-8">
<title>Valtrix 4 Management Limited</title>
<link rel="stylesheet" href="https://fonts.googleapis.com/css2?family=Michroma&family=Questrial&family=Ubuntu:wght@300;400&family=Arimo:wght@400;700&display=swap">
<style>
:root{
  --blue:#1a6ccc;
  --blue-deep:#1f72c9;
  --nav-bg:#c8daeb;
  --nav-text:#6b7886;
  --page-bg:#e6e6e6;
  --text:#6e6e6e;
  --list-text:#6a6a6a;
  --red:#cc1111;
  --footer:#6b6b6b;
  --footer-dark:#565656;
  --logo-grey:#6d6d6d;
}
*{margin:0;padding:0;box-sizing:border-box}
html,body{width:1200px;height:1136px;overflow:hidden;background:var(--page-bg)}
body{position:relative;font-family:"Ubuntu",sans-serif;color:var(--text)}
.abs{position:absolute}

.site-header{left:0;top:0;width:1200px;height:170px;background:linear-gradient(#f4f4f4,#e4e6e9)}
.brand-dot{left:248px;top:22px;width:70px;height:70px;border-radius:50%;background:var(--blue-deep)}
.brand-name{left:178px;top:116px;font-family:"Questrial",sans-serif;font-size:33px;letter-spacing:6.4px;color:var(--logo-grey);line-height:1;white-space:nowrap}
.brand-sub{left:178px;top:148px;font-family:"Questrial",sans-serif;font-size:12.5px;letter-spacing:3.4px;color:var(--logo-grey);line-height:1;white-space:nowrap}
.top-links{top:45px;font-family:"Arimo",sans-serif;font-size:12.5px;color:#555;display:flex;align-items:center;gap:4px}
.social{top:101px;width:36px;height:36px;border-radius:6px}

.hero-band{left:0;top:170px;width:1200px;height:296px;background:linear-gradient(90deg,#1e6fc6,#9cc6ee 50%,#1e6fc6)}
.hero-photo{left:170px;top:170px;width:859px;height:296px;background:linear-gradient(100deg,#6c7076 0%,#a7abb0 35%,#d6d9dc 60%,#eef0f2 100%)}

.main-nav{left:0;top:466px;width:1200px;height:34px;background:var(--nav-bg)}
.main-nav a{position:absolute;top:13px;font-family:"Michroma",sans-serif;font-size:8.6px;color:var(--nav-text);text-decoration:none;white-space:nowrap}

.content-panel{left:170px;top:503px;width:588px;height:498px;background:linear-gradient(#f7f7f7,#ececec);border:1px solid #e0e0e0}
.side-panel{left:767px;top:503px;width:261px;height:498px;background:linear-gradient(#f7f7f7,#ececec);border:1px solid #dcdcdc}

.welcome{left:187px;top:519px;font-family:"Questrial",sans-serif;font-size:24px;font-weight:400;color:#707070;white-space:nowrap}
.welcome b{font-weight:400;color:var(--blue)}
.intro{left:187px;top:549px;width:554px;font-size:11px;line-height:16.3px;text-align:justify;font-weight:300;letter-spacing:.25px;color:#666}
.more{font-family:"Arimo",sans-serif;font-size:9.5px;color:var(--red);white-space:nowrap}
.section-title{font-family:"Michroma",sans-serif;font-style:italic;font-weight:400;font-size:12px;color:var(--blue);white-space:nowrap}

.card{border-radius:8px;background:linear-gradient(#fbfbfb,#f0f0f0);border:1px solid #dcdcdc}
.card-photo{border:1px solid #c9c9c9}
.item{font-family:"Arimo",sans-serif;font-weight:700;font-size:11px;color:var(--list-text);white-space:nowrap;display:flex;align-items:center;gap:6px}
.item svg{flex:none}

.side-title{font-family:"Michroma",sans-serif;font-style:italic;font-weight:400;font-size:12px;color:#777;white-space:nowrap}
.group-title{font-family:"Michroma",sans-serif;font-style:italic;font-weight:400;font-size:9.6px;color:var(--blue);white-space:nowrap}
.ref{font-family:"Arimo",sans-serif;font-size:12px;color:var(--list-text);white-space:nowrap;display:flex;align-items:center;gap:4px}
.rule{left:777px;width:221px;border-top:1px dotted #a0a0a0}
.partners{left:777px;top:865px;width:239px;height:117px;background:#f7f7f7;border:1px solid #d5d5d5}
.partner{width:112px;height:51px;background:#fff;display:flex;align-items:center;justify-content:center}
.partner span{display:block;width:64px;height:18px;border-radius:3px}

.site-footer{left:0;top:1004px;width:1200px;height:107px;background:var(--footer)}
.footer-nav a{position:absolute;top:1016px;font-family:"Arimo",sans-serif;font-size:9.5px;color:#fff;text-decoration:none;white-space:nowrap}
.copyright{left:0;top:1091px;width:1200px;text-align:center;font-size:9.5px;color:#e2e2e2;font-weight:300}
.footer-rule{left:0;top:1111px;width:1200px;height:2px;background:#cfcfcf}
.footer-base{left:0;top:1113px;width:1200px;height:17px;background:var(--footer-dark)}
</style>
</head>
<body>

<header class="abs site-header"></header>
<div class="abs brand-dot"></div>
<div class="abs brand-name">VALTRIX 4</div>
<div class="abs brand-sub">MANAGEMENT LIMITED</div>

<div class="abs top-links" style="left:855px">
  <svg width="13" height="11" viewBox="0 0 13 11"><path d="M1 6 6.5 1 12 6" fill="none" stroke="#c33" stroke-width="1.6"/><rect x="3" y="6" width="7" height="5" fill="#999"/></svg>HOME
</div>
<div class="abs top-links" style="left:923px">
  <svg width="14" height="10" viewBox="0 0 14 10"><rect x=".5" y=".5" width="13" height="9" fill="#eef4fb" stroke="#7aa6d6"/><path d="M.5 .5 7 6 13.5 .5" fill="none" stroke="#7aa6d6"/></svg>CONTACT US
</div>

<div class="abs social" style="left:837px;background:#3b5fa8"></div>
<div class="abs social" style="left:886px;background:#4fb9e6"></div>
<div class="abs social" style="left:936px;background:#c62a24"></div>
<div class="abs social" style="left:983px;background:#1f7fbd"></div>

<div class="abs hero-band"></div>
<div class="abs hero-photo" role="img" aria-label="Photo of three colleagues in business attire gathered around a laptop"></div>

<nav class="abs main-nav">
  <a style="left:185px">ABOUT US</a>
  <a style="left:279px">INTRODUCTION</a>
  <a style="left:403px">PROJECT CONTROL</a>
  <a style="left:556px">CONTRACT MANAGEMENT</a>
  <a style="left:752px">SPECIALIST SERVICES</a>
  <a style="left:923px">PROJECTS</a>
</nav>

<main>
  <div class="abs content-panel"></div>
  <h1 class="abs welcome">Welcome to Valtrix <b>4</b> Management Limited</h1>
  <p class="abs intro">Valtrix 4 Management Limited provide project control and contract management expertise to the Engineering / Construction and Manufacturing industries. We are able to draw from the vast experience of our specialist resource base. Our employees have considerable experience gained from direct involvement on numerous large scale international projects. These projects include Civil, Building, Infrastructure and Defense with particular focus on the Rail and Aviation transportation sectors. Our employees possess the practical experience necessary to implement world class Project Control / Project Management systems and processes..</p>
  <a class="abs more" style="left:692px;top:662px">View details</a>

  <h2 class="abs section-title" style="left:191px;top:687px">Control Systems We Provide by Discipline:</h2>
  <div class="abs card" style="left:191px;top:710px;width:551px;height:117px"></div>
  <div class="abs card-photo" style="left:199px;top:722px;width:115px;height:92px;background:linear-gradient(120deg,#d9dfe6,#9fb0c4 60%,#eef1f4)" role="img" aria-label="Photo of a businesswoman ticking a checklist"></div>
  <div class="abs item" style="left:328px;top:724px"><svg width="8" height="10"><path d="M.5.5h5l2 2v7h-7z" fill="#fff" stroke="#4a86c8"/><path d="M2 4h4M2 6h4" stroke="#4a86c8"/></svg>General</div>
  <div class="abs item" style="left:328px;top:743px"><svg width="8" height="10"><path d="M.5.5h5l2 2v7h-7z" fill="#fff" stroke="#4a86c8"/><path d="M2 4h4M2 6h4" stroke="#4a86c8"/></svg>Schedule</div>
  <div class="abs item" style="left:328px;top:762px"><svg width="8" height="10"><path d="M.5.5h5l2 2v7h-7z" fill="#fff" stroke="#4a86c8"/><path d="M2 4h4M2 6h4" stroke="#4a86c8"/></svg>ControlReporting</div>
  <div class="abs item" style="left:328px;top:781px"><svg width="8" height="10"><path d="M.5.5h5l2 2v7h-7z" fill="#fff" stroke="#4a86c8"/><path d="M2 4h4M2 6h4" stroke="#4a86c8"/></svg>Material / Sub Contract Control</div>
  <div class="abs item" style="left:328px;top:800px"><svg width="8" height="10"><path d="M.5.5h5l2 2v7h-7z" fill="#fff" stroke="#4a86c8"/><path d="M2 4h4M2 6h4" stroke="#4a86c8"/></svg>Reporting</div>
  <div class="abs item" style="left:527px;top:724px"><svg width="8" height="10"><path d="M.5.5h5l2 2v7h-7z" fill="#fff" stroke="#4a86c8"/><path d="M2 4h4M2 6h4" stroke="#4a86c8"/></svg>Claim Analysis</div>
  <div class="abs item" style="left:527px;top:743px"><svg width="8" height="10"><path d="M.5.5h5l2 2v7h-7z" fill="#fff" stroke="#4a86c8"/><path d="M2 4h4M2 6h4" stroke="#4a86c8"/></svg>Change Control</div>
  <div class="abs item" style="left:527px;top:762px"><svg width="8" height="10"><path d="M.5.5h5l2 2v7h-7z" fill="#fff" stroke="#4a86c8"/><path d="M2 4h4M2 6h4" stroke="#4a86c8"/></svg>Risk &amp; Opportunity Management</div>
  <div class="abs item" style="left:527px;top:781px"><svg width="8" height="10"><path d="M.5.5h5l2 2v7h-7z" fill="#fff" stroke="#4a86c8"/><path d="M2 4h4M2 6h4" stroke="#4a86c8"/></svg>Governance</div>
  <a class="abs more" style="left:681px;top:804px">View details</a>

  <h2 class="abs section-title" style="left:191px;top:848px">Our Specialist Services:</h2>
  <div class="abs card" style="left:191px;top:870px;width:551px;height:117px"></div>
  <div class="abs card-photo" style="left:199px;top:883px;width:115px;height:92px;background:linear-gradient(160deg,#cfe3ee,#9fc0d6 55%,#e6eef3)" role="img" aria-label="Photo of a team meeting in a bright office"></div>
  <div class="abs item" style="left:328px;top:885px"><svg width="8" height="10"><path d="M.5.5h5l2 2v7h-7z" fill="#fff" stroke="#4a86c8"/><path d="M2 4h4M2 6h4" stroke="#4a86c8"/></svg>Engineering Earned Value</div>
  <div class="abs item" style="left:328px;top:904px"><svg width="8" height="10"><path d="M.5.5h5l2 2v7h-7z" fill="#fff" stroke="#4a86c8"/><path d="M2 4h4M2 6h4" stroke="#4a86c8"/></svg>S-Curve Reporting</div>
  <div class="abs item" style="left:328px;top:923px"><svg width="8" height="10"><path d="M.5.5h5l2 2v7h-7z" fill="#fff" stroke="#4a86c8"/><path d="M2 4h4M2 6h4" stroke="#4a86c8"/></svg>Critical Issues Reporting</div>
  <div class="abs item" style="left:328px;top:942px"><svg width="8" height="10"><path d="M.5.5h5l2 2v7h-7z" fill="#fff" stroke="#4a86c8"/><path d="M2 4h4M2 6h4" stroke="#4a86c8"/></svg>Six Sigma</div>
  <div class="abs item" style="left:328px;top:961px"><svg width="8" height="10"><path d="M.5.5h5l2 2v7h-7z" fill="#fff" stroke="#4a86c8"/><path d="M2 4h4M2 6h4" stroke="#4a86c8"/></svg>Coaching / Mentoring / Training</div>
  <div class="abs item" style="left:529px;top:887px"><svg width="8" height="10"><path d="M.5.5h5l2 2v7h-7z" fill="#fff" stroke="#4a86c8"/><path d="M2 4h4M2 6h4" stroke="#4a86c8"/></svg>Six Sigma</div>
  <div class="abs item" style="left:529px;top:905px"><svg width="8" height="10"><path d="M.5.5h5l2 2v7h-7z" fill="#fff" stroke="#4a86c8"/><path d="M2 4h4M2 6h4" stroke="#4a86c8"/></svg>Coaching / Mentoring / Training</div>
  <a class="abs more" style="left:681px;top:965px">View details</a>
</main>

<aside>
  <div class="abs side-panel"></div>
  <h2 class="abs side-title" style="left:777px;top:526px">Our reference projects:</h2>

  <h3 class="abs group-title" style="left:777px;top:559px">RAIL - PROJECTS</h3>
  <div class="abs ref" style="left:783px;top:577px"><svg width="8" height="10"><path d="M.5.5h5l2 2v7h-7z" fill="#fff" stroke="#4a86c8"/><path d="M2 4h4M2 6h4" stroke="#4a86c8"/></svg>Northvale Rapid Rail Link</div>
  <div class="abs ref" style="left:783px;top:595px"><svg width="8" height="10"><path d="M.5.5h5l2 2v7h-7z" fill="#fff" stroke="#4a86c8"/><path d="M2 4h4M2 6h4" stroke="#4a86c8"/></svg>Harbour City West Rail</div>
  <div class="abs ref" style="left:783px;top:613px"><svg width="8" height="10"><path d="M.5.5h5l2 2v7h-7z" fill="#fff" stroke="#4a86c8"/><path d="M2 4h4M2 6h4" stroke="#4a86c8"/></svg>Midland Route Modernization</div>
  <div class="abs ref" style="left:783px;top:631px"><svg width="8" height="10"><path d="M.5.5h5l2 2v7h-7z" fill="#fff" stroke="#4a86c8"/><path d="M2 4h4M2 6h4" stroke="#4a86c8"/></svg>Metro Cross Link</div>
  <div class="abs ref" style="left:783px;top:649px"><svg width="8" height="10"><path d="M.5.5h5l2 2v7h-7z" fill="#fff" stroke="#4a86c8"/><path d="M2 4h4M2 6h4" stroke="#4a86c8"/></svg>Meridian Line Extension Project</div>
  <div class="abs rule" style="top:674px"></div>

  <h3 class="abs group-title" style="left:775px;top:682px">AVIATION - PROJECTS</h3>
  <div class="abs ref" style="left:783px;top:700px"><svg width="8" height="10"><path d="M.5.5h5l2 2v7h-7z" fill="#fff" stroke="#4a86c8"/><path d="M2 4h4M2 6h4" stroke="#4a86c8"/></svg>New Carrow International Airport</div>
  <div class="abs ref" style="left:783px;top:718px"><svg width="8" height="10"><path d="M.5.5h5l2 2v7h-7z" fill="#fff" stroke="#4a86c8"/><path d="M2 4h4M2 6h4" stroke="#4a86c8"/></svg>Selby Point International Airport</div>
  <div class="abs rule" style="top:744px"></div>

  <h3 class="abs group-title" style="left:777px;top:752px">MANUFACTURING - PROJECTS</h3>
  <div class="abs ref" style="left:783px;top:770px"><svg width="8" height="10"><path d="M.5.5h5l2 2v7h-7z" fill="#fff" stroke="#4a86c8"/><path d="M2 4h4M2 6h4" stroke="#4a86c8"/></svg>Alpenrail Twin-Deck FV Coach</div>
  <div class="abs rule" style="top:793px"></div>

  <h3 class="abs group-title" style="left:777px;top:801px">BUILDING</h3>
  <div class="abs ref" style="left:783px;top:819px"><svg width="8" height="10"><path d="M.5.5h5l2 2v7h-7z" fill="#fff" stroke="#4a86c8"/><path d="M2 4h4M2 6h4" stroke="#4a86c8"/></svg>Larkspur Shopping Centre</div>
  <div class="abs ref" style="left:783px;top:837px"><svg width="8" height="10"><path d="M.5.5h5l2 2v7h-7z" fill="#fff" stroke="#4a86c8"/><path d="M2 4h4M2 6h4" stroke="#4a86c8"/></svg>Orvane Head Office</div>
  <a class="abs more" style="left:962px;top:845px">View details</a>

  <div class="abs partners"></div>
  <div class="abs partner" style="left:782px;top:870px"><span style="background:#c9b37a"></span></div>
  <div class="abs partner" style="left:899px;top:870px"><span style="background:#c8202a"></span></div>
  <div class="abs partner" style="left:782px;top:927px"><span style="background:#8a2a2a"></span></div>
  <div class="abs partner" style="left:899px;top:927px"><span style="background:#7fcfc0"></span></div>
</aside>

<footer>
  <div class="abs site-footer"></div>
  <nav class="footer-nav">
    <a style="left:267px">HOME</a>
    <a style="left:304px">ABOUT US</a>
    <a style="left:368px">INTRODUCTION</a>
    <a style="left:454px">PROJECT CONTROL</a>
    <a style="left:561px">CONTRACT MANAGEMENT</a>
    <a style="left:695px">SPECIALIST SERVICES</a>
    <a style="left:813px">PROJECTS</a>
    <a style="left:873px">CONTACT US</a>
  </nav>
  <p class="abs copyright">Copyright 2012 Valtrix4 Management Limited. All rights reserved.</p>
  <div class="abs footer-rule"></div>
  <div class="abs footer-base"></div>
</footer>

</body>
</html>
```